Melodrop Icon design for single song release

Design an icon for melodrop (eventually, we will need to use the same style to design the 4 side CD cover) for a new song to be released. Needs to follow certain specs: I am attaching a design that I created, but looking for the design to be spiced up a bit. I am happy with the design, font, and style.. Just want to see something a bit more creative.
Specs:
1. An Melodrop ICON for my latest single that i need to get released. Here are the specs..
• Finalized design for icon for Melodrop: (DLT Logo attached and JPEG dimensions below)
o Name of the song is “HOW”
Melodrop: Your cover art must be:
o 1400 x 1400 pixels
o JPG file type
o 72 - 300dpi (300dpi is the best)
o Less than 25mb
o RGB color scheme (not CMYK)

I have my music logo and the picture, so I have to have something that fits these dimensions for Melodrop.

Please do not change the photo. and please keep the photo in color. The song has an edge to it, but don't want over the top.

Target Market(s)

Contemporary Christian; Christian Rock - music has an edge.

Font styles to use
Other font styles liked:
• see example design

Requirements
Must have
• Delphine Tavory
• Song title "How"
• Photo
• Dimensions listed above when design if final.
• Photo attached
• Logo attached
• *Please use a color photo; please use the lettering like the example; and the font colors

```html
<!DOCTYPE html>
<html lang="en">
<head>
<meta charset="utf-8">
<title>Delphine Tavory – HOW</title>
<link rel="stylesheet" href="https://fonts.googleapis.com/css2?family=Nunito+Sans:wght@400&display=swap">
<style>
  :root {
    --page-bg: #b4b4b4;
    --cover-black: #000000;
    --name-red: #b3212b;
    --name-grey: #a9a9a9;
    --title-grey: #b5b5b5;
    --badge-fill: #141414;
    --badge-border: #5a55a8;
    --badge-text: #f2f2f2;
  }
  * { margin: 0; padding: 0; box-sizing: border-box; }
  html, body {
    width: 1200px;
    height: 1000px;
    overflow: hidden;
    background: var(--page-bg);
    font-family: "Nunito Sans", "Avenir Next", Arial, sans-serif;
  }
  .cover {
    position: absolute;
    left: 266px;
    top: 167px;
    width: 667px;
    height: 666px;
    background: var(--cover-black);
    overflow: hidden;
  }
  .artist-strip {
    position: absolute;
    left: 0;
    top: 0;
    width: 117px;
    height: 100%;
    display: flex;
    align-items: center;
    justify-content: center;
  }
  .artist-name {
    writing-mode: vertical-rl;
    transform: rotate(180deg);
    font-size: 56px;
    font-weight: 400;
    letter-spacing: 4px;
    line-height: 1;
    white-space: nowrap;
  }
  .artist-first { color: var(--name-red); }
  .artist-last { color: var(--name-grey); }
  .portrait {
    position: absolute;
    left: 117px;
    top: 0;
    width: 434px;
    height: 100%;
    background:
      radial-gradient(ellipse 42% 38% at 55% 48%, #d9a58f 0%, #c99580 55%, rgba(201,149,128,0) 100%),
      linear-gradient(180deg, #e8d3a6 0%, #d9bd86 40%, #b9955e 62%, #2a2522 80%, #0c0b0b 100%);
  }
  .logo-badge {
    position: absolute;
    left: 565px;
    top: 14px;
    width: 87px;
    height: 87px;
    background: var(--badge-fill);
    border: 2px solid var(--badge-border);
    display: flex;
    align-items: center;
    justify-content: center;
    color: var(--badge-text);
    font-size: 26px;
    font-weight: 400;
    letter-spacing: 1px;
  }
  .song-title-box {
    position: absolute;
    left: 431px;
    top: 550px;
    width: 236px;
    height: 70px;
    background: var(--cover-black);
    display: flex;
    align-items: center;
    padding-left: 38px;
  }
  .song-title {
    color: var(--title-grey);
    font-size: 52px;
    font-weight: 400;
    letter-spacing: 8px;
    line-height: 1;
  }
</style>
</head>
<body>
  <main class="cover">
    <div class="artist-strip">
      <h1 class="artist-name"><span class="artist-first">DELPHINE</span><span class="artist-last">TAVORY</span></h1>
    </div>
    <div class="portrait" role="img" aria-label="Colour portrait photo of the artist with long blonde hair, wearing a black turtleneck"></div>
    <div class="logo-badge">DLT</div>
    <div class="song-title-box">
      <h2 class="song-title">HOW</h2>
    </div>
  </main>
</body>
</html>
```